Custom Truck shop New Business Card design

double sided business card including my new logo, brand colors and picking a font I attached, clean and modern look. I attached the old card for some reference. and would like to include the picture of the white truck attached. I would also like to have it with one of my employees info as well. (same info except name and title Brin Tolvay Service Writer)

Dale Porvick
Owner

address
48310 E Calloway Ridge Rd S
STE 217
Marsh Hollow, CO 80219

phone 720-555-0184

email dale@brokenspurrigs.example

website brokenspurrgis.example

social @brokenspurrigs

Target Market(s)

men 18-60

Industry/Entity Type

Automotive

Contact Information for Business Card

Dale Porvick Owner address 48310 E Calloway Ridge Rd S STE 217 Marsh Hollow, CO 80219 phone 720-555-0184 email dale@brokenspurrigs.example website brokenspurrgis.example social @brokenspurrigs

Font styles to use
Other font styles liked:
• fonts attached

Requirements
Must have
• new logo, orange #FC68D, Charcoal #333333
Nice to have
• the white truck

```html
<!DOCTYPE html>
<html lang="en">
<head>
<meta charset="utf-8">
<title>Broken Spur Rigs – Business Card</title>
<link rel="stylesheet" href="https://fonts.googleapis.com/css2?family=Archivo+Black&family=Open+Sans:wght@400;600;700&display=swap">
<style>
  :root {
    --bg: #222222;
    --charcoal: #333333;
    --charcoal-deep: #2b2b2b;
    --charcoal-low: #262626;
    --orange: #f26b2c;
    --white: #ffffff;
    --photo-a: #8c8d91;
    --photo-b: #4a4b4f;
    --photo-c: #34382f;
  }
  * { box-sizing: border-box; margin: 0; padding: 0; }
  html, body { width: 1200px; height: 780px; overflow: hidden; background: var(--bg); }
  body { font-family: "Open Sans", Arial, sans-serif; color: var(--white); }

  .canvas {
    width: 1200px; height: 780px;
    display: flex; align-items: center; justify-content: center; gap: 70px;
  }
  .card {
    position: relative;
    width: 360px; height: 630px;
    border-radius: 26px;
    overflow: hidden;
    box-shadow: 0 18px 40px rgba(0,0,0,.55);
  }

  /* Front: truck photo side */
  .card-front { background: var(--charcoal); }
  .truck-photo {
    position: absolute; inset: 0;
    background:
      radial-gradient(ellipse at 55% 45%, var(--photo-a) 0%, var(--photo-b) 55%, transparent 80%),
      linear-gradient(160deg, var(--photo-b) 0%, var(--photo-a) 45%, var(--photo-c) 100%);
    opacity: .85;
  }
  .front-brand {
    position: absolute; top: 60px; right: 24px;
    transform-origin: top right;
    transform: rotate(-90deg) translateY(-100%);
    display: flex; align-items: center; gap: 16px;
    white-space: nowrap;
  }
  .front-brand .brand-dot { width: 60px; height: 60px; transform: rotate(90deg); }
  .front-brand .brand-name { font-size: 30px; }

  /* Shared brand lockup */
  .brand-dot {
    display: block; border-radius: 50%;
    background: var(--white); border: 5px solid var(--orange);
  }
  .brand-name {
    font-family: "Open Sans", Arial, sans-serif;
    font-weight: 600; letter-spacing: 2px; text-transform: uppercase;
    color: var(--white);
    border-bottom: 2px solid var(--orange);
    padding-bottom: 4px;
  }

  /* Back: contact side */
  .card-back { background: var(--charcoal); text-align: center; }
  .back-wave {
    position: absolute; left: 0; right: 0; bottom: 0; height: 200px;
    background: var(--charcoal-low);
  }
  .back-wave svg { position: absolute; top: -60px; left: 0; width: 100%; height: 120px; }

  .back-brand { margin-top: 44px; display: flex; flex-direction: column; align-items: center; gap: 12px; }
  .back-brand .brand-dot { width: 66px; height: 66px; }
  .back-brand .brand-name { font-size: 24px; }

  .person { margin-top: 34px; }
  .person-name { font-family: "Archivo Black", Arial, sans-serif; font-size: 34px; line-height: 1; }
  .person-name .first { color: var(--orange); }
  .person-title { font-family: "Archivo Black", Arial, sans-serif; font-size: 19px; margin-top: 6px; }

  .icon-row { display: flex; justify-content: center; gap: 8px; margin-top: 18px; }
  .icon {
    width: 24px; height: 24px; border-radius: 50%;
    background: var(--orange);
    display: flex; align-items: center; justify-content: center;
  }
  .icon svg { width: 14px; height: 14px; }

  .phone { font-family: "Open Sans", Arial, sans-serif; font-weight: 700; font-size: 30px; margin-top: 8px; letter-spacing: .5px; }
  .contact-line { font-size: 14px; margin-top: 2px; }

  .address-block { margin-top: 22px; position: relative; z-index: 1; }
  .address-block .icon { margin: 0 auto 12px; }
  .address { font-size: 15px; line-height: 1.45; }

  .social { position: absolute; left: 0; right: 0; bottom: 40px; z-index: 1; }
  .social-row { display: flex; justify-content: center; gap: 8px; }
  .social-dot { width: 24px; height: 24px; border-radius: 50%; background: var(--orange); }
  .social-handle { font-size: 15px; margin-top: 8px; }
</style>
</head>
<body>
<main class="canvas">

  <section class="card card-front" aria-label="Card front">
    <div class="truck-photo" role="img" aria-label="Photo of a lifted white pickup truck with large chrome wheels parked on a street"></div>
    <div class="front-brand">
      <span class="brand-dot"></span>
      <span class="brand-name">Broken Spur Rigs</span>
    </div>
  </section>

  <section class="card card-back" aria-label="Card back">
    <div class="back-wave">
      <svg viewBox="0 0 360 120" preserveAspectRatio="none" aria-hidden="true">
        <path d="M0 60 Q180 150 360 20 L360 120 L0 120 Z" fill="#262626"/>
        <path d="M0 60 Q180 150 360 20" fill="none" stroke="#1e1e1e" stroke-width="3"/>
      </svg>
    </div>

    <div class="back-brand">
      <span class="brand-dot"></span>
      <span class="brand-name">Broken Spur Rigs</span>
    </div>

    <div class="person">
      <h1 class="person-name"><span class="first">Dale</span> Porvick</h1>
      <p class="person-title">Owner</p>
    </div>

    <div class="icon-row">
      <span class="icon"><svg viewBox="0 0 24 24"><path fill="#fff" d="M6.6 10.8a15 15 0 006.6 6.6l2.2-2.2a1 1 0 011-.25 11.4 11.4 0 003.6.57 1 1 0 011 1V20a1 1 0 01-1 1A17 17 0 013 4a1 1 0 011-1h3.5a1 1 0 011 1c0 1.25.2 2.45.57 3.57a1 1 0 01-.25 1z"/></svg></span>
      <span class="icon"><svg viewBox="0 0 24 24"><path fill="#fff" d="M3 5h18v14H3z"/><path fill="none" stroke="#f26b2c" stroke-width="2" d="M3 6l9 7 9-7"/></svg></span>
      <span class="icon"><svg viewBox="0 0 24 24"><circle cx="12" cy="12" r="9" fill="none" stroke="#fff" stroke-width="2"/><path fill="none" stroke="#fff" stroke-width="1.6" d="M3 12h18M12 3c3 3 3 15 0 18M12 3c-3 3-3 15 0 18"/></svg></span>
    </div>

    <p class="phone">720-555-0184</p>
    <p class="contact-line">www.brokenspurrgis.example</p>
    <p class="contact-line">dale@brokenspurrigs.example</p>

    <div class="address-block">
      <span class="icon"><svg viewBox="0 0 24 24"><path fill="#fff" d="M12 2a7 7 0 00-7 7c0 5 7 13 7 13s7-8 7-13a7 7 0 00-7-7zm0 9.5A2.5 2.5 0 1112 6.5a2.5 2.5 0 010 5z"/></svg></span>
      <p class="address">48310 E Calloway Ridge Rd S<br>STE 217 Marsh Hollow, CO 80219</p>
    </div>

    <div class="social">
      <div class="social-row">
        <span class="social-dot"></span>
        <span class="social-dot"></span>
      </div>
      <p class="social-handle">@brokenspurrigs</p>
    </div>
  </section>

</main>
</body>
</html>
```